Plonkara

We need a design for a mobile app (Android & iOS) with the following features:
- Recommend other applications based on different criteria, such as similar applications, hot apps, apps installed by friends and so on.
- Recommend a featured app everyday.
- List installed apps on the device.
- List harmful or malicious installed apps on the device
- List hot apps according to the more used apps by the comunity or the user's friends
- Profiles: Save the list of apps installed on the device as a list to allow the user to restore them on other devices.

Industry/Entity Type

Android

Requirements
Must have
• Find attached to this project a mockup of the screen elements desired.
To put it in a nutshell, the main elements are:
- Main Menu: A main menu to access the other modules of the app

- Recommended Apps: List of apps recommended, each app will display: icon, title, price, the reason(s) why it was recommended (can be expandable if takes too much room), a button to install and a button to ignore the advice.

- Application of the day: A screen that contains the icon of the app, its rating, some screenshots, a short description or promotional text, and a button to install the app. It must be also available a way to display the history and see the recommended applications the previous days.

- Installed Apps: A list with the apps on the device. It will show the app's icon, name, package, size and a button to share the app.

- Harmful apps: List of dangerous apps found on the device. It will show the icon of the app and the name. A visual and textual indicator to measure the dangerous, and the reasons of the report. It will also includes a button to ignore the advice and another one to uninstall the application.

- Login/My account: These screens will be used to login and manage the account. The account management options are listed on the attached document.

- Profiles: The design must include the proper screens and dialogs to: save a profile, restore a profile (install the missing apps on the device), show the apps saved on the profile.

- Hot Apps: The app must allow to filter between the hot apps and the hot apps installed by the user's friends. For each app, must show: the icon, name and a trending indicator in order to say if the app is winning or losing popularity

- Miscellaneous: Other features required:
+ Login screen: The login is made in two steps. First, the user introduce their email. If the email is already registered, enters the password. Otherwise, register a new account introducing a password twice (password + repeat password, please check the attached file for more info).
+ Password recovery and password change screens
+ Loading splash (shown at the start of the application for 2-4 seconds)
+ A proper layout to inform about errors / messages in empty lists, (for example if no harmful apps where found).
+ A proper layout for loading process, for example when scanning for harmful apps.
+ Vectorial App Icon: At least one icon for the app (512 x512 px)
+ Vectorial Featured (1024x500 px) and Promo banners (180x120 px) for Veltrano Shop.
+ For the UI elements like buttons or checkboxes is required the following status: normal, pressed, disabled and focused.
Nice to have
• Examples of apps with nice designs:

Brimwell: https://shop.veltrano.example/items/details?id=com.brimwell
Tidal Ledger: https://shop.veltrano.example/items/details?id=com.marvesto.tidal
KOV Coastal Terminals: https://tunestack.example/es/app/kov-coastal-terminals/id804172259?mt=8
Should not have
• The app should not have garish or poorly contrasted colors and icons.

```html
<!DOCTYPE html>
<html lang="en">
<head>
<meta charset="utf-8">
<title>Plonkara – App Manager screens</title>
<link rel="stylesheet" href="https://fonts.googleapis.com/css2?family=Roboto+Condensed:wght@400;700&display=swap">
<style>
  :root {
    --page: #ffffff;
    --status-bg: #2b2b2b;
    --status-text: #e6e6e6;
    --header-dark: #24361b;
    --header-light: #33501f;
    --row-bg: #222222;
    --row-pressed: #000000;
    --row-divider: #4d6b3a;
    --row-text: #f2f2f2;
    --icon-grey: #8a8a8a;
    --field-top: #1f2f17;
    --field-bottom: #456d31;
    --splash-deep: #2b4a1f;
    --splash-mid: #4b7a37;
    --splash-light: #6a9a52;
    --title-band: #1b2e10;
    --wall-top: #2e4d25;
    --wall-bottom: #7aa76a;
  }
  * { box-sizing: border-box; margin: 0; padding: 0; }
  html, body { width: 1200px; height: 883px; overflow: hidden; background: var(--page); }
  body { position: relative; font-family: "Roboto Condensed", "Arial Narrow", sans-serif; }

  .menu-screen {
    position: absolute; left: 22px; top: 14px; width: 570px; height: 854px;
    background: linear-gradient(180deg, var(--field-top) 0%, var(--field-bottom) 100%);
    overflow: hidden;
  }
  .status-bar {
    height: 34px; background: var(--status-bg); color: var(--status-text);
    display: flex; align-items: center; justify-content: center; position: relative;
    font-size: 24px; font-weight: 700;
  }
  .status-bar .signal { position: absolute; left: 10px; top: 10px; }
  .status-bar .battery { position: absolute; right: 12px; top: 9px; }
  .app-header {
    height: 96px; display: flex; align-items: center; justify-content: center;
    background: repeating-linear-gradient(135deg, var(--header-light) 0 2px, var(--header-dark) 2px 5px);
    color: #ffffff; font-size: 38px; font-weight: 400;
    border-bottom: 1px solid #111;
  }
  .menu-list { list-style: none; }
  .menu-item {
    height: 64px; display: flex; align-items: center; background: var(--row-bg);
    border-bottom: 1px solid var(--row-divider); color: var(--row-text); font-size: 25px;
  }
  .menu-item.is-pressed { background: var(--row-pressed); }
  .menu-item .item-icon { width: 36px; height: 36px; margin: 0 26px 0 18px; flex: none; }
  .menu-item .item-label { flex: 1; }
  .menu-item .chevron { width: 16px; height: 22px; margin-right: 22px; }

  .splash-screen {
    position: absolute; left: 617px; top: 19px; width: 562px; height: 843px; overflow: hidden;
  }
  .splash-screen svg { display: block; }
</style>
</head>
<body>

<section class="menu-screen" aria-label="Main menu">
  <div class="status-bar">
    <svg class="signal" width="34" height="14" viewBox="0 0 34 14" aria-hidden="true">
      <rect x="0" y="10" width="4" height="4" fill="#e6e6e6"/><rect x="6" y="8" width="4" height="6" fill="#e6e6e6"/>
      <rect x="12" y="5" width="4" height="9" fill="#e6e6e6"/><rect x="18" y="2" width="4" height="12" fill="#e6e6e6"/>
      <rect x="24" y="0" width="4" height="14" fill="#e6e6e6"/>
    </svg>
    <span class="clock">4:20 PM</span>
    <svg class="battery" width="36" height="17" viewBox="0 0 36 17" aria-hidden="true">
      <rect x="1" y="1" width="30" height="15" fill="none" stroke="#e6e6e6" stroke-width="2"/>
      <rect x="32" y="5" width="3" height="7" fill="#e6e6e6"/><rect x="4" y="4" width="10" height="9" fill="#e6e6e6"/>
    </svg>
  </div>
  <header class="app-header">App Manager</header>
  <ul class="menu-list">
    <li class="menu-item">
      <svg class="item-icon" viewBox="0 0 36 36" aria-hidden="true"><path d="M3 16h6v16H3zM11 16l7-12c3 0 4 2 3 5l-1 5h10c2 0 3 2 2 4l-3 11c-1 2-2 3-4 3H11z" fill="var(--icon-grey)"/></svg>
      <span class="item-label">Recommended Apps</span>
      <svg class="chevron" viewBox="0 0 16 22" aria-hidden="true"><path d="M3 2l10 9-10 9" fill="none" stroke="#ddd" stroke-width="3.5"/></svg>
    </li>
    <li class="menu-item">
      <svg class="item-icon" viewBox="0 0 36 36" aria-hidden="true"><rect x="2" y="8" width="26" height="25" fill="none" stroke="var(--icon-grey)" stroke-width="2.5"/><rect x="2" y="8" width="26" height="6" fill="var(--icon-grey)"/><text x="7" y="29" font-size="13" font-family="Roboto Condensed, sans-serif" fill="var(--icon-grey)">17</text><path d="M28 0l2.5 5.5 6 .6-4.5 4 1.3 6-5.3-3-5.3 3 1.3-6-4.5-4 6-.6z" fill="#bdbdbd"/></svg>
      <span class="item-label">Application of the day</span>
      <svg class="chevron" viewBox="0 0 16 22" aria-hidden="true"><path d="M3 2l10 9-10 9" fill="none" stroke="#ddd" stroke-width="3.5"/></svg>
    </li>
    <li class="menu-item is-pressed">
      <svg class="item-icon" viewBox="0 0 36 36" aria-hidden="true"><path d="M18 2l9 10h-6v10h-6V12H9z" fill="var(--icon-grey)"/><path d="M3 20v13h30V20" fill="none" stroke="var(--icon-grey)" stroke-width="4"/></svg>
      <span class="item-label">Installed Apps</span>
      <svg class="chevron" viewBox="0 0 16 22" aria-hidden="true"><path d="M3 2l10 9-10 9" fill="none" stroke="#ddd" stroke-width="3.5"/></svg>
    </li>
    <li class="menu-item">
      <svg class="item-icon" viewBox="0 0 36 36" aria-hidden="true"><path d="M18 1l3 7 7-4-1 8 8 2-6 5 6 5-8 2 1 8-7-4-3 7-3-7-7 4 1-8-8-2 6-5-6-5 8-2-1-8 7 4z" fill="var(--icon-grey)"/></svg>
      <span class="item-label">Harmful Apps</span>
      <svg class="chevron" viewBox="0 0 16 22" aria-hidden="true"><path d="M3 2l10 9-10 9" fill="none" stroke="#ddd" stroke-width="3.5"/></svg>
    </li>
    <li class="menu-item">
      <svg class="item-icon" viewBox="0 0 36 36" aria-hidden="true"><path d="M17 35C8 35 4 28 6 20c1-5 5-8 4-14 5 3 6 8 6 12 2-4 3-9 1-17 8 5 13 13 13 21 0 8-5 13-13 13z" fill="none" stroke="var(--icon-grey)" stroke-width="2.5"/><path d="M18 33c-4 0-6-3-5-7 1-3 3-4 3-7 3 2 6 5 6 9 0 3-2 5-4 5z" fill="var(--icon-grey)"/></svg>
      <span class="item-label">Hot Apps</span>
      <svg class="chevron" viewBox="0 0 16 22" aria-hidden="true"><path d="M3 2l10 9-10 9" fill="none" stroke="#ddd" stroke-width="3.5"/></svg>
    </li>
  </ul>
</section>

<section class="splash-screen" aria-label="Loading splash">
  <svg width="562" height="843" viewBox="0 0 562 843">
    <defs>
      <radialGradient id="splash-glow" cx="0.62" cy="0.5" r="0.75">
        <stop offset="0" stop-color="var(--splash-light)"/>
        <stop offset="0.55" stop-color="var(--splash-mid)"/>
        <stop offset="1" stop-color="var(--splash-deep)"/>
      </radialGradient>
      <linearGradient id="icon-wall" x1="0" y1="0" x2="0" y2="1">
        <stop offset="0" stop-color="var(--wall-top)"/>
        <stop offset="1" stop-color="var(--wall-bottom)"/>
      </linearGradient>
      <radialGradient id="globe-fill" cx="0.6" cy="0.4" r="0.7">
        <stop offset="0" stop-color="#4f7d3c"/>
        <stop offset="1" stop-color="#2c4a20"/>
      </radialGradient>
      <linearGradient id="cart-fill" x1="0" y1="0" x2="1" y2="1">
        <stop offset="0" stop-color="#8fb0c8"/>
        <stop offset="1" stop-color="#c9503a"/>
      </linearGradient>
    </defs>
    <rect class="splash-background" width="562" height="843" fill="url(#splash-glow)"/>
    <path class="icon-wall" role="img" aria-label="Perspective wall of many colourful app icons" d="M0 0H562V138C520 240 390 312 190 312C110 312 50 306 0 298Z" fill="url(#icon-wall)"/>
    <circle class="icon-globe" role="img" aria-label="Green sphere covered with faint app icons" cx="134" cy="648" r="198" fill="url(#globe-fill)" opacity="0.85"/>
    <rect class="app-cart" role="img" aria-label="Shopping cart filled with colourful app icons" x="339" y="608" width="173" height="125" rx="14" fill="url(#cart-fill)" opacity="0.85"/>
    <path class="title-lettering" role="img" aria-label="Curved hand-lettered App Manager title" d="M 92 428 A 262 262 0 0 1 310 712" fill="none" stroke="var(--title-band)" stroke-width="46" stroke-linecap="round" opacity="0.35"/>
  </svg>
</section>

</body>
</html>
```